Design CD-Velvet Tadpole/WAIT FOR THE ORANGE TRAIN
Zielgruppe
Wir sind Velvet Tadpole eine INDIE/ALTERNATIVE Band.. bestehend aus 4 Jungs im alter von durchschnittlich 22 Jahren. Wir suchen ein Design für unsere 2. Platte die den Namen 'WAIT FOR THE ORANGE TRAIN' trägt. Im gleichnamigen Song geht es um einen Menschen der am Limit lebt und jeden Moment ohne Rücksicht auf andere auskostet.. als er eines Tages versteht wie er den Menschen die er liebt damit Schaden zufügt, verspricht er seiner LIEBE:'I SWEAR I WILL WAIT FOR THE ORANGE TRAIN'..'im nächsten Leben werde ich ein besserer Typ sein.
Unsere Musik zeichnet sich durch 3 Stimmigen Gesang, verspielte teilweise psychodelische Sounds und eingängige Melodien die sich zu unserem Markenzeichen entwickelt haben aus.
Aufgabenstellung
Das Design soll Modern,verspielt,Bunt, gerne etwas abstrakt und vor allem Grafisch (nicht im realistic style) sein.
Beispielbilder in welche Richtung es gehen soll lege ich in den Anhang.

```html
<!DOCTYPE html>
<html lang="en">
<head>
<meta charset="utf-8">
<title>Velvet Tadpole – Wait for the Orange Train</title>
<link rel="stylesheet" href="https://fonts.googleapis.com/css2?family=Alfa+Slab+One&family=Archivo+Black&display=swap">
<style>
  :root {
    --paper: #f4f6f4;
    --ink-blue: #1f7fc4;
    --ink-teal: #1aa3a0;
    --ink-deep: #0d3550;
    --ink-orange: #e08a1c;
    --floor-mist: #b9d4d6;
    --floor-dark: #2b3d3f;
    --floor-deepest: #142022;
    --title-fill: #f6f49c;
    --title-edge: #1a1a14;
    --chrome-light: #e9eeee;
    --chrome-dark: #6d7b7c;
  }
  * { margin: 0; padding: 0; box-sizing: border-box; }
  html, body {
    width: 1200px;
    height: 1200px;
    overflow: hidden;
    background: var(--floor-deepest);
  }
  .cover {
    position: relative;
    width: 1200px;
    height: 1200px;
    overflow: hidden;
    background: var(--paper);
  }
  .cover-art {
    position: absolute;
    inset: 0;
    background:
      linear-gradient(to bottom,
        rgba(43,61,63,0) 0%,
        rgba(43,61,63,0) 58%,
        rgba(185,212,214,0.55) 70%,
        rgba(43,61,63,0.85) 84%,
        var(--floor-deepest) 100%),
      radial-gradient(ellipse 28% 18% at 12% 60%, rgba(224,138,28,0.85), transparent 70%),
      radial-gradient(ellipse 22% 14% at 82% 38%, rgba(224,138,28,0.8), transparent 70%),
      radial-gradient(ellipse 30% 26% at 28% 30%, rgba(26,163,160,0.9), transparent 72%),
      radial-gradient(ellipse 45% 22% at 60% 44%, rgba(31,127,196,0.85), transparent 72%),
      radial-gradient(ellipse 18% 30% at 8% 12%, rgba(31,127,196,0.8), transparent 70%),
      radial-gradient(ellipse 25% 30% at 90% 10%, rgba(13,53,80,0.75), transparent 70%),
      radial-gradient(ellipse 35% 18% at 45% 62%, rgba(13,53,80,0.55), transparent 70%),
      var(--paper);
  }
  .cover-type {
    position: absolute;
    inset: 0;
    width: 1200px;
    height: 1200px;
  }
  .band-name {
    font-family: "Alfa Slab One", serif;
    font-size: 96px;
    fill: var(--title-fill);
    stroke: var(--title-edge);
    stroke-width: 5px;
    paint-order: stroke fill;
  }
  .album-title {
    font-family: "Archivo Black", sans-serif;
    font-size: 112px;
    fill: url(#chrome);
    stroke: var(--floor-deepest);
    stroke-width: 3px;
    paint-order: stroke fill;
  }
</style>
</head>
<body>
  <main class="cover">
    <div class="cover-art" role="img" aria-label="Abstract ink painting: flowing blue, teal and dark navy ink strokes with orange splashes on white, reflected on a misty surface fading to dark teal"></div>
    <svg class="cover-type" viewBox="0 0 1200 1200" aria-label="Velvet Tadpole – Wait for the Orange Train">
      <defs>
        <linearGradient id="chrome" x1="0" y1="1140" x2="0" y2="1230" gradientUnits="userSpaceOnUse">
          <stop offset="0" stop-color="var(--chrome-light)"/>
          <stop offset="0.55" stop-color="var(--chrome-dark)"/>
          <stop offset="1" stop-color="var(--chrome-light)"/>
        </linearGradient>
      </defs>
      <text class="band-name" x="600" y="1128" text-anchor="middle">Velvet Tadpole</text>
      <text class="album-title" x="0" y="1222" textLength="1200" lengthAdjust="spacingAndGlyphs">WAIT FOR THE ORANGE TRAIN</text>
    </svg>
  </main>
</body>
</html>
```